Create Brisk Lesson Studio a card design that will stick in the mind of prospects.

Brisk Lesson Studio specialises designs and produces training video, animation, illustration and text.

We need a card design that oozes class and leaves the prospect brimming with confidence.

The design will feature the Brisk Lesson Studio all black logo (uploaded). The design may also use the shade of orange from the orange version of the logo (uploaded). Note, just the color is to be used e.g. for the back of the card, not the orange logo itself.

The Brisk brand is about authenticity, quality, maturity and assurance. We are a safe buy when it comes to the prospects next project.

Target Market(s)

The primary target is training managers or others who are responsible for choosing to hire companies to produce their training media e.g. video. This will usually be a large spend so they need to have confidence.

Industry/Entity Type

Training

Contact Information for Business Card

FRONT:

Brisk Lesson Studio
Phone: 03 5172 4039
1st Floor, 418 Kellerby Road
Mt Ferncombe
VIC 3862
Australia
www.brisklesson.com.au

Lionel Petch
Founder and Lead Consultant
mobile: +61 3 0462 735 218
email: lionel@brisklesson.com.au

BACK:
Specialising in design and production of training:

video
animation
illustration
text

for delivery via internet, intranet and/or LMS.

Number of Pages Required

4 page

Font styles to use
Sans Serif

Requirements
Must have
• The black logo uploaded with the brief.
Nice to have
• The inclusion of the shade of orange found in the orange logo also uploaded with the brief. One example would be having the back of the card in this orange and using a white font for the text. But I want the designer to work this out.
Should not have
• No colours other than black and the orange included in the uploaded orange logo.

```html
<!DOCTYPE html>
<html lang="en">
<head>
<meta charset="utf-8">
<title>Brisk Lesson Studio – Business Card Front and Back</title>
<link rel="stylesheet" href="https://fonts.googleapis.com/css2?family=Poppins:wght@400;500;600;700&family=Raleway:wght@300;400&display=swap">
<style>
  :root {
    --stage: #3b3b3c;
    --paper: #ffffff;
    --ink: #231f20;
    --orange: #e8511f;
    --peach: #f4a585;
    --heading: #ffffff;
  }
  * { margin: 0; padding: 0; box-sizing: border-box; }
  html, body { width: 1200px; height: 723px; overflow: hidden; background: var(--stage); }
  .canvas { position: relative; width: 1200px; height: 723px; background: var(--stage); font-family: "Poppins", sans-serif; color: var(--ink); }

  .section-title {
    position: absolute; left: 40px; top: 170px;
    font-family: "Raleway", sans-serif; font-weight: 300;
    font-size: 30px; letter-spacing: 0.5px; color: var(--heading);
  }

  .card {
    position: absolute; top: 222px; width: 540px; height: 310px;
    background: var(--paper); overflow: hidden;
    box-shadow: 0 4px 14px rgba(0,0,0,0.45);
  }
  .card--front { left: 40px; }
  .card--back { left: 620px; }

  .card__art { position: absolute; inset: 0; }

  .contact { position: absolute; left: 57px; font-size: 13.5px; line-height: 19px; font-weight: 400; }
  .contact--company { top: 40px; }
  .contact--person { top: 200px; }
  .contact__name { color: var(--orange); font-weight: 500; font-size: 16px; line-height: 22px; }
  .contact__line { display: flex; align-items: center; gap: 7px; }
  .contact__line svg { width: 10px; height: 10px; flex: none; margin-left: -17px; }

  .logo-name {
    position: absolute; font-family: "Poppins", sans-serif; font-weight: 700;
    color: var(--ink); text-align: center;
  }
  .card--front .logo-name { left: 356px; top: 88px; width: 144px; font-size: 38px; line-height: 48px; }
  .card--back .logo-name { left: 0; right: 0; top: 40px; font-size: 46px; line-height: 56px; }

  .back-tagline {
    position: absolute; left: 0; right: 0; top: 160px; text-align: center;
    font-size: 12.5px; font-weight: 600; letter-spacing: 0.2px; text-transform: uppercase;
  }
  .services { position: absolute; left: 40px; right: 40px; top: 196px; display: flex; justify-content: space-between; padding: 0 20px; }
  .service { display: flex; flex-direction: column; align-items: center; gap: 8px; font-size: 12px; font-weight: 600; text-transform: uppercase; }
  .service svg { height: 18px; }
  .back-note { position: absolute; left: 0; right: 0; top: 262px; text-align: center; font-size: 12.5px; }
</style>
</head>
<body>
<main class="canvas">
  <h1 class="section-title">BUSINESS CARD FRONT AND BACK</h1>

  <section class="card card--front" aria-label="Business card front">
    <svg class="card__art" viewBox="0 0 540 310" aria-hidden="true">
      <polygon points="478,0 494,0 478,160" fill="var(--peach)"/>
      <polygon points="478,0 488,0 478,120" fill="var(--orange)"/>
      <polygon points="381,170 381,310 345,310" fill="var(--peach)"/>
      <polygon points="381,190 381,310 362,310" fill="var(--orange)"/>
      <rect x="381" y="0" width="97" height="310" fill="var(--ink)"/>
      <circle cx="428" cy="112" r="74" fill="var(--paper)"/>
    </svg>
    <div class="logo-name">Brisk</div>

    <div class="contact contact--company">
      <p class="contact__name">Brisk Lesson Studio</p>
      <p class="contact__line"><svg viewBox="0 0 10 10"><path d="M2 0.5 L4 2.5 L3 4 Q4.5 6 6 7 L7.5 6 L9.5 8 L8 9.5 Q3 9 0.5 2 Z" fill="var(--orange)"/></svg>03 5172 4039</p>
      <p>1st Floor, 418 Kellerby Road</p>
      <p>Mt Ferncombe</p>
      <p>VIC 3862</p>
      <p>Australia</p>
      <p class="contact__line"><svg viewBox="0 0 10 10"><circle cx="5" cy="5" r="4.5" fill="var(--orange)"/><path d="M0.5 5 H9.5 M5 0.5 V9.5" stroke="var(--paper)" stroke-width="0.8"/></svg>brisklesson.com.au</p>
    </div>

    <div class="contact contact--person">
      <p class="contact__name">Lionel Petch</p>
      <p>Founder and Lead Consultant</p>
      <p class="contact__line"><svg viewBox="0 0 10 10"><rect x="2.5" y="0" width="5" height="10" rx="1" fill="var(--orange)"/><rect x="3.5" y="1.5" width="3" height="6" fill="var(--paper)"/></svg>+61 3 0462 735 218</p>
      <p class="contact__line"><svg viewBox="0 0 10 10"><rect x="0" y="2" width="10" height="7" rx="1" fill="var(--orange)"/><path d="M0.5 2.5 L5 6 L9.5 2.5" stroke="var(--paper)" stroke-width="0.9" fill="none"/></svg>lionel@brisklesson.com.au</p>
    </div>
  </section>

  <section class="card card--back" aria-label="Business card back">
    <div class="logo-name">Brisk</div>
    <p class="back-tagline">Specialising in design and production of training:</p>
    <div class="services">
      <div class="service">
        <svg viewBox="0 0 24 18" width="24"><rect x="1" y="3" width="15" height="12" rx="1.5" fill="var(--orange)"/><polygon points="16,9 23,4 23,14" fill="var(--orange)"/></svg>
        Video
      </div>
      <div class="service">
        <svg viewBox="0 0 30 18" width="30"><circle cx="8" cy="9" r="5" fill="var(--peach)"/><circle cx="14" cy="9" r="5" fill="#ee7a4f"/><circle cx="21" cy="9" r="6" fill="var(--orange)"/></svg>
        Animation
      </div>
      <div class="service">
        <svg viewBox="0 0 18 18" width="18"><polygon points="9,1 15,9 12,17 6,17 3,9" fill="var(--orange)"/><circle cx="9" cy="10" r="1.6" fill="var(--paper)"/><line x1="9" y1="1" x2="9" y2="9" stroke="var(--paper)" stroke-width="0.9"/></svg>
        Illustration
      </div>
      <div class="service">
        <svg viewBox="0 0 22 18" width="22"><path d="M5 2 H2 V16 H5 M17 2 H20 V16 H17" stroke="var(--orange)" stroke-width="1.3" fill="none"/><path d="M7 5 H15 M11 5 V14" stroke="var(--orange)" stroke-width="1.6"/></svg>
        Text
      </div>
    </div>
    <p class="back-note">for delivery via internet, intranet and/or LMS.</p>
  </section>
</main>
</body>
</html>
```